A5 Patient Information Booklet (Chiropractic Clinic) 4-8 pages

Here’s a polished, professional rewrite of your full brief and content, with clearer structure, corrected language, and a premium tone:

---

**Project Title:** Premium Patient Information Brochure (Chiropractic & Wellness Clinic)

---

### **Overview**

We are a health and wellness clinic seeking a premium, high-end patient information brochure to provide following a patient’s initial consultation and first treatment.

The purpose of this booklet is to:

* Reinforce trust and professionalism
* Help patients understand what to expect next
* Encourage adherence to care recommendations
* Position the clinic as calm, expert-led, and results-driven

---

### **Format**

* 4–8 page booklet (A5 or similar size)
* Print-ready and digital versions required

---

### **Target Audience**

Patients who have just completed their initial consultation and may have begun treatment. They may already be experiencing physical or mental changes, so the brochure should guide, reassure, and educate them on what comes next.

---

### **Tone & Style**

* Premium, calm, and reassuring
* Modern wellness aesthetic (not overly clinical)
* Clean layout with minimal clutter
* Soft, neutral colour palette (whites, creams, muted greens, soft blues)
* Elegant typography (e.g. Montserrat / Lato)
* High-end, trustworthy, and professional feel

---

### **Key Messages**

#### 1. Listen to Your Body

Patients may feel different after treatment. Reassure them that this is normal and part of the healing process.

#### 2. Post-Treatment Advice

* Stay well hydrated
* Rest if needed
* Avoid overexertion if the body requires recovery

#### 3. Healing is a Journey (Core Concept)

A strong visual metaphor of a **“road to recovery”** or **journey** should be central to the design.

This journey should clearly illustrate three phases:

* **Phase 1: Initial Care (Weeks 1–6)**
Focus: Reducing pain/discomfort, calming the body, and initiating response to treatment

* **Phase 2: Corrective Care (Weeks 6–12)**
Focus: Addressing underlying issues, improving function, and creating lasting change

* **Phase 3: Wellness / Maintenance (Ongoing)**
Focus: Maintaining progress, preventing relapse, and supporting long-term wellbeing

**Important:**

* Emphasise that this is not a quick fix
* Progress requires time and consistency
* Each patient follows an individualised care plan
* The journey should feel structured, positive, and achievable

#### 4. Personalised Care

Reinforce that every treatment plan is tailored specifically to the individual.

#### 5. Professional Reassurance

Patients should feel confident they are in expert hands and supported throughout their journey.

---

### **Design Direction**

* Use imagery that reflects calmness, progression, and wellness (e.g. pathways, nature, soft gradients)
* Avoid generic stock imagery
* **Only use original clinic images from website and social media**
* Prioritise white space and clarity
* Aim for a luxury spa/medical hybrid aesthetic

---

## **Content Structure (Page-by-Page)**

### **Front Cover**

* Clean, minimal, premium design
* Clinic branding

---

### **Page 1: Patient Case Summary**

**Title:** *Welcome to Fernwell Practice*

Thank you for choosing Fernwell Practice.

This booklet is designed to guide you through:

* What we found during your initial consultation
* Your personalised recommended treatment plan
* Your road to recovery
* Long-term wellness care
* Why we take the approach we do

---

### **Page 2: Your Care Journey**

**Stage 1: Your Initial Consultation**

Today we completed a comprehensive assessment of your health and function, including:

* Full case history and discussion of your symptoms and goals
* Orthopaedic and neurological testing
* Postural and movement assessment
* Initial treatment (where appropriate)

**What this tells us:**

* How your body is currently functioning
* Where areas of stress or dysfunction may be present
* The most appropriate and effective path forward for your care

---

### **Page 3: Your Suggested Treatment Plan**

Based on today’s findings, your recommended care plan is:

**______ treatments over ______ weeks**

This should be viewed alongside your *Road to Recovery* to help you understand what to expect.

We have also discussed:

* Expected timelines for improvement
* Available payment options

**After Treatment:**
It is common to feel different following treatment. This is a normal response as your body begins to adapt and respond.

We recommend:

* Staying well hydrated
* Allowing time for rest and recovery
* Avoiding overexertion if your body feels it needs it

---

### **Page 4: What to Expect Next**

Healing is not always linear—it is a process that occurs over time.

Your care will typically progress through the following stages:

* **Relief Care**
Focused on reducing discomfort and calming the body

* **Corrective Care**
Focused on addressing underlying issues and improving function
(This phase may include prescribed exercises)

* **Maintenance / Wellness Care**
Focused on sustaining progress, preventing recurrence, and supporting long-term health

---

### **Page 5: Understanding Chiropractic Care**

**What is Chiropractic?**
Chiropractic care focuses on the relationship between the spine, nervous system, and overall body function.

By improving spinal movement and alignment, chiropractic care helps support the nervous system, allowing the body to function and heal more effectively.

**About Fernwell Practice**
At Fernwell Practice, our approach is centred around personalised, patient-focused care. We aim to not only relieve symptoms but to address underlying causes and support long-term wellbeing.

---

### **Back Page**

* Clinic contact details
* Website
* Social media icons/handles

**Closing Message:**
“A healthier, stronger you—supported every step of the way.”

---

### **Deliverables**

* Print-ready PDF
* Editable source files

---

### **Additional Notes**

* The brochure should feel valuable and worth keeping
* Encourage long-term care in a subtle, non-pushy way
* Maintain clarity, readability, and strong visual hierarchy
* Balance professionalism with warmth and approachability

---

If you’d like, I can also turn this into **actual brochure copy (fully written, patient-facing text)** or help you refine it further for a designer.

Target Market(s)

Existing patients who want to feel better and look after themselves that is given after their initil consultation appointment

Industry/Entity Type

Chiropractic, wellness, health

Font styles to use
Other font styles liked:
• Montserrat or Lato

Colors
0094D4
00A9DD
6FCCEA
C7EBF8
E9F6FB
00AB8E
00BBA5
67D7C9
C6EFE9
E9F9F6
6B429C
8869AF
B7A5CE
E3DAEB
F3F0F8

Requirements
Must have
• my own photos, look premium wellness, be clear and simple to understand for patients journey or what to expect next and over time
Nice to have
• USe my social media/website for ideas
Should not have
• generic photos and images

```html
<!DOCTYPE html>
<html lang="en">
<head>
<meta charset="utf-8">
<title>Fernwell Practice – Patient Booklet</title>
<link href="https://fonts.googleapis.com/css2?family=Montserrat:wght@400;500;600;700;800&family=Lato:wght@400;700&family=Dancing+Script:wght@500&display=swap" rel="stylesheet">
<style>
:root{
  --teal:#0e8c7e;
  --teal-dark:#0a6f66;
  --teal-soft:#c6efe9;
  --teal-mist:#e9f9f6;
  --purple:#6b429c;
  --purple-soft:#8869af;
  --lilac:#f3f0f8;
  --ink:#1f2326;
  --body:#4a4f55;
  --line:#c9ccd0;
  --page:#ffffff;
  --canvas:#f1f1f1;
  --red:#e5412f;
  --orange:#f29a1d;
  --green:#7fae3a;
}
*{box-sizing:border-box;margin:0;padding:0}
html,body{width:1200px;height:800px;overflow:hidden;background:var(--canvas)}
body{position:relative;font-family:'Lato',sans-serif;color:var(--body)}
h1,h2,h3{font-weight:500}
.page{position:absolute;background:var(--page);overflow:hidden;box-shadow:0 1px 4px rgba(0,0,0,.12)}
.abs{position:absolute}
.heading{font-family:'Montserrat',sans-serif}

/* cover */
.cover{left:9px;top:9px;width:569px;height:393px}
.cover-photo{position:absolute;inset:0;background:
  linear-gradient(180deg,rgba(255,255,255,0) 55%,rgba(198,239,233,.9) 100%),
  linear-gradient(90deg,#f4f4f4 0%,#d8d8d8 35%,#8a8a8a 65%,#5c5c5c 100%)}
.brand-mark{width:44px;height:44px;border-radius:50%;border:2px solid var(--teal)}
.brand-name{font-family:'Montserrat',sans-serif;font-weight:600;color:var(--ink);letter-spacing:.3px;white-space:nowrap}
.brand-sub{font-family:'Montserrat',sans-serif;font-weight:600;color:var(--teal);letter-spacing:1.4px;white-space:nowrap}
.cover .brand-mark{left:82px;top:27px}
.cover .brand-name{left:0;width:208px;text-align:center;top:82px;font-size:13px}
.cover .brand-sub{left:0;width:208px;text-align:center;top:100px;font-size:7px}
.cover-title{left:32px;top:218px;font-family:'Montserrat',sans-serif;line-height:.98}
.cover-title .lead{display:block;font-size:36px;font-weight:500;color:var(--ink)}
.cover-title .main{display:block;font-size:42px;font-weight:800;color:var(--teal);letter-spacing:.5px}
.cover-rule{left:34px;top:348px;width:28px;height:2px;background:var(--teal)}
.cover-tag{left:34px;top:357px;font-size:13px;color:var(--ink)}

/* after treatment */
.after{left:588px;top:9px;width:603px;height:393px}
.small-mark{width:26px;height:26px;border-radius:50%;border:1.5px solid var(--teal)}
.after .small-mark{left:28px;top:11px}
.page-title{font-family:'Montserrat',sans-serif;font-weight:500;font-size:16.5px;line-height:1.15;color:var(--ink)}
.page-title .accent{color:var(--teal)}
.after .page-title{left:27px;top:56px}
.rule{height:2px;width:24px;background:var(--teal)}
.after .rule{left:28px;top:95px}
.intro{left:27px;top:111px;width:160px;font-size:7.6px;line-height:1.55;color:var(--ink)}
.intro p+p{margin-top:6px}
.tips{left:16px;top:184px;width:184px;height:215px;background:#f3f5f5;border-radius:10px;padding:4px 8px 0 8px}
.tip{display:flex;gap:10px;padding:6px 0;border-bottom:1px solid #dde1e1}
.tip:last-child{border-bottom:0}
.tip-icon{flex:0 0 32px;height:32px;border-radius:50%;background:#e4ebea;display:flex;align-items:center;justify-content:center}
.tip-title{font-family:'Montserrat',sans-serif;font-size:7.4px;font-weight:600;color:var(--teal);margin-bottom:2px}
.tip-text{font-size:6px;line-height:1.45;color:var(--ink)}
.divider-v{width:1px;background:var(--line)}
.after .divider-v{left:218px;top:108px;height:285px}
.side{left:240px;top:112px;width:150px}
.side-title{font-family:'Montserrat',sans-serif;font-size:9.6px;font-weight:600;color:var(--teal);margin-bottom:8px}
.side p{font-size:7.2px;line-height:1.6;color:var(--ink);margin-bottom:7px}
.benefits{list-style:none;margin-top:4px}
.benefits li{display:flex;align-items:center;gap:7px;font-size:7.2px;color:var(--ink);margin-bottom:9px}
.help-title{margin-top:24px}
.after-photo{left:406px;top:0;width:197px;height:393px;border-radius:26px 0 0 26px;
  background:linear-gradient(160deg,#efe9e2 0%,#d9c8b6 40%,#8b6f56 70%,#4a5568 100%)}

/* journey */
.journey{left:9px;top:411px;width:569px;height:377px}
.section-title{font-family:'Montserrat',sans-serif;font-weight:500;color:var(--purple)}
.chiro-title{left:34px;top:30px;font-size:11px}
.chiro-title+.rule{left:34px;top:47px;width:34px;background:var(--purple-soft)}
.portrait{left:12px;top:65px;width:76px;height:76px;border-radius:50%;
  background:radial-gradient(circle at 50% 45%,#d8b79a 0%,#b58a66 45%,#e9e9ea 80%)}
.chiro-text{left:97px;top:76px;width:112px;font-size:5.8px;line-height:1.6;color:var(--ink)}
.chiro-text p+p{margin-top:8px}
.journey .divider-v{left:212px;top:18px;height:214px}
.journey-title{left:213px;width:356px;top:17px;text-align:center;font-family:'Montserrat',sans-serif;font-size:13px;font-weight:500;color:var(--teal)}
.journey-sub{left:213px;width:356px;top:36px;text-align:center;font-size:7.5px;line-height:1.55;color:var(--ink)}
.road{left:225px;top:68px;width:330px;height:56px;border-radius:28px;
  background:linear-gradient(90deg,#f6c3bb 0%,#fbdcae 35%,#dcebc0 65%,#c6efe9 100%)}
.phase-card{top:134px;width:84px;height:100px;background:#fff;border-radius:6px;box-shadow:0 1px 4px rgba(0,0,0,.14);padding:7px 6px 0;text-align:center}
.phase-label{font-family:'Montserrat',sans-serif;font-weight:600;font-size:8px}
.phase-name{font-family:'Montserrat',sans-serif;font-size:6.6px;color:var(--ink);margin-top:3px}
.phase-weeks{font-size:6px;color:var(--ink);margin-top:3px}
.phase-list{text-align:left;margin-top:6px;padding-left:10px;font-size:5.8px;line-height:1.35;color:var(--ink)}
.phase-list li{margin-bottom:4px}
.p1 .phase-label{color:var(--red)}
.p2 .phase-label{color:var(--orange)} .p2 li::marker{color:var(--orange)}
.p3 .phase-label{color:var(--teal)} .p3 li::marker{color:var(--teal)}
.rule-h{left:34px;top:248px;width:515px;height:1px;background:var(--line)}
.about-mark{left:28px;top:274px;width:40px;height:40px;border-radius:50%;border:1.5px solid var(--teal)}
.about-title{left:95px;top:266px;font-size:9px}
.about-text{left:95px;top:284px;width:430px;font-size:6.3px;color:var(--ink)}
.about-text p{margin-bottom:9px}
.corner{right:0;bottom:0}
.page-num{right:24px;bottom:10px;font-family:'Montserrat',sans-serif;font-size:12px;color:#fff}

/* care plan + back */
.plan{left:588px;top:411px;width:603px;height:377px}
.plan-panel{left:0;top:0;width:258px;height:377px;background:var(--lilac)}
.plan-title{left:22px;top:33px;font-size:12.5px;font-weight:500;color:var(--ink);white-space:nowrap}
.plan-title .accent{color:var(--purple-soft)}
.plan-panel .rule{left:22px;top:52px;width:28px;background:var(--purple-soft)}
.field-label{font-size:8.3px;color:var(--ink)}
.field-line{height:1px;background:#8e8e96}
.contact-panel{left:258px;top:0;width:345px;height:377px}
.contact-panel .brand-mark{left:147px;top:9px;width:48px;height:48px}
.contact-panel .brand-name{left:0;width:345px;text-align:center;top:65px;font-size:13px}
.contact-panel .brand-sub{left:0;width:345px;text-align:center;top:82px;font-size:6.8px}
.script{left:0;width:345px;text-align:center;top:96px;font-family:'Dancing Script',cursive;font-size:16px;color:var(--teal)}
.script-follow{left:0;width:345px;text-align:center;top:120px;font-size:11px;color:var(--ink)}
.contact-panel .rule{left:63px;top:143px;width:30px;background:var(--teal)}
.contact-list{left:62px;top:158px;list-style:none}
.contact-list li{display:flex;align-items:center;gap:12px;font-size:7.8px;color:var(--ink);height:20px}
.socials{left:62px;top:242px;display:flex;gap:17px}
.social-dot{width:24px;height:24px;border-radius:50%;background:var(--teal)}
.closing{left:0;top:292px;width:345px;height:85px;background:linear-gradient(100deg,var(--teal-dark) 0%,#16867e 45%,#4b6aa0 80%,var(--purple-soft) 100%);color:#fff}
.closing-icon{left:38px;top:18px}
.closing-text{left:81px;top:20px;font-size:8.6px;line-height:1.6}
.closing-script{left:81px;top:56px;font-family:'Dancing Script',cursive;font-size:12px}
</style>
</head>
<body>

<section class="page cover">
  <div class="cover-photo" role="img" aria-label="Black and white photo of a chiropractor treating a patient's back, fading to soft teal"></div>
  <div class="abs brand-mark"></div>
  <div class="abs brand-name">FERNWELL PRACTICE</div>
  <div class="abs brand-sub">CHIROPRACTIC &amp; WELLNESS</div>
  <h1 class="abs cover-title"><span class="lead">YOUR</span><span class="main">ROAD TO</span><span class="main">RECOVERY</span></h1>
  <div class="abs cover-rule"></div>
  <p class="abs cover-tag">A personalised journey to better health.</p>
</section>

<section class="page after">
  <div class="abs small-mark"></div>
  <h2 class="abs page-title">WHAT TO EXPECT<br><span class="accent">AFTER YOUR TREATMENT</span></h2>
  <div class="abs rule"></div>
  <div class="abs intro">
    <p>It's completely normal to feel different after your treatment.</p>
    <p>As your body begins to respond and adapt, you may notice changes in movement, tension, or overall wellbeing.</p>
  </div>
  <div class="abs tips">
    <div class="tip">
      <div class="tip-icon"><svg width="16" height="16" viewBox="0 0 16 16"><path d="M8 2 C5 6 4 8 4 10 a4 4 0 0 0 8 0 C12 8 11 6 8 2Z" fill="none" stroke="#0e8c7e" stroke-width="1.2"/></svg></div>
      <div><div class="tip-title">STAY HYDRATED</div><div class="tip-text">Drinking plenty of water supports your body's natural recovery process.</div></div>
    </div>
    <div class="tip">
      <div class="tip-icon"><svg width="16" height="16" viewBox="0 0 16 16"><circle cx="8" cy="5" r="2.8" fill="none" stroke="#0e8c7e" stroke-width="1.2"/><path d="M2.5 14 c0-3.5 2.5-5 5.5-5 s5.5 1.5 5.5 5" fill="none" stroke="#0e8c7e" stroke-width="1.2"/></svg></div>
      <div><div class="tip-title">LISTEN TO YOUR BODY</div><div class="tip-text">You may feel relief, mild soreness, or changes in how your body moves—these are all normal signs of adjustment.</div></div>
    </div>
    <div class="tip">
      <div class="tip-icon"><svg width="18" height="14" viewBox="0 0 18 14"><path d="M1 2 V12 M1 9 H17 V12 M6 9 V5 H15 a2 2 0 0 1 2 2 V9" fill="none" stroke="#0e8c7e" stroke-width="1.2"/><circle cx="3.8" cy="6.5" r="1.6" fill="none" stroke="#0e8c7e" stroke-width="1.1"/></svg></div>
      <div><div class="tip-title">REST WHEN NEEDED</div><div class="tip-text">Give your body time to recover. Avoid overexertion if your body feels like it needs rest.</div></div>
    </div>
    <div class="tip">
      <div class="tip-icon"><svg width="16" height="16" viewBox="0 0 16 16"><path d="M8 14 C3 11 3 5 8 2 C13 5 13 11 8 14Z M8 14 V5" fill="none" stroke="#0e8c7e" stroke-width="1.2"/></svg></div>
      <div><div class="tip-title">TRUST THE PROCESS</div><div class="tip-text">Meaningful, lasting change takes time. Each step of your care plan is designed to support long-term results—not just short-term relief.</div></div>
    </div>
  </div>
  <div class="abs divider-v"></div>
  <div class="abs side">
    <h3 class="side-title">What is Chiropractic Care?</h3>
    <p>Chiropractic care focuses on restoring proper movement and function within the body, particularly the spine and nervous system.</p>
    <p>By improving alignment and reducing tension, your body can move more freely, recover more effectively, and function at its best.</p>
    <h3 class="side-title help-title">How It Helps You</h3>
    <ul class="benefits">
      <li><svg width="10" height="10" viewBox="0 0 10 10"><circle cx="5" cy="5" r="4.3" fill="none" stroke="#0e8c7e"/><path d="M3 5.2 L4.5 6.6 L7.2 3.6" fill="none" stroke="#0e8c7e"/></svg>Reduces pain and discomfort</li>
      <li><svg width="10" height="10" viewBox="0 0 10 10"><circle cx="5" cy="5" r="4.3" fill="none" stroke="#0e8c7e"/><path d="M3 5.2 L4.5 6.6 L7.2 3.6" fill="none" stroke="#0e8c7e"/></svg>Improves mobility and flexibility</li>
      <li><svg width="10" height="10" viewBox="0 0 10 10"><circle cx="5" cy="5" r="4.3" fill="none" stroke="#0e8c7e"/><path d="M3 5.2 L4.5 6.6 L7.2 3.6" fill="none" stroke="#0e8c7e"/></svg>Supports nervous system function</li>
      <li><svg width="10" height="10" viewBox="0 0 10 10"><circle cx="5" cy="5" r="4.3" fill="none" stroke="#0e8c7e"/><path d="M3 5.2 L4.5 6.6 L7.2 3.6" fill="none" stroke="#0e8c7e"/></svg>Enhances overall wellbeing</li>
    </ul>
  </div>
  <div class="abs after-photo" role="img" aria-label="Photo of the chiropractor smiling while adjusting a seated patient's back"></div>
</section>

<section class="page journey">
  <h2 class="abs section-title chiro-title">YOUR CHIROPRACTOR</h2>
  <div class="abs rule"></div>
  <div class="abs portrait" role="img" aria-label="Portrait photo of chiropractor Clara"></div>
  <div class="abs chiro-text">
    <p>At Fernwell Practice, your care is led by chiropractor Clara, who takes a personalised, hands-on approach to your health.</p>
    <p>Every consultation is focused on understanding your body, your lifestyle, and your goals—so your treatment plan is tailored specifically to you.</p>
    <p>Clara combines clinical expertise with a calm, supportive environment to help you feel confident, informed, and in control of your recovery journey.</p>
  </div>
  <div class="abs divider-v"></div>
  <h2 class="abs journey-title">YOUR RECOVERY JOURNEY</h2>
  <p class="abs journey-sub">Healing is a journey, not a quick fix.<br>With the right care and consistency, lasting change is possible.</p>
  <div class="abs road" role="img" aria-label="Illustration of a winding road to recovery, red to orange to teal, with three numbered phase markers ending in an arrow"></div>
  <div class="abs phase-card p1" style="left:243px">
    <div class="phase-label">PHASE 1</div><div class="phase-name">INITIAL CARE</div><div class="phase-weeks">(WEEKS 1–6)</div>
    <ul class="phase-list"><li>Reduce pain &amp; discomfort</li><li>Calm your body</li><li>Begin healing response</li></ul>
  </div>
  <div class="abs phase-card p2" style="left:354px">
    <div class="phase-label">PHASE 2</div><div class="phase-name">CORRECTIVE CARE</div><div class="phase-weeks">(WEEKS 6–12)</div>
    <ul class="phase-list"><li>Address underlying issues</li><li>Improve movement &amp; function</li><li>Build stability</li></ul>
  </div>
  <div class="abs phase-card p3" style="left:465px">
    <div class="phase-label">PHASE 3</div><div class="phase-name">WELLNESS CARE</div><div class="phase-weeks">(ONGOING)</div>
    <ul class="phase-list"><li>Maintain progress</li><li>Prevent future issues</li><li>Support long-term wellbeing</li></ul>
  </div>
  <div class="abs rule-h"></div>
  <div class="abs about-mark"></div>
  <h3 class="abs section-title about-title">ABOUT FERNWELL PRACTICE</h3>
  <div class="abs about-text">
    <p>At Fernwell Practice, we believe that true health is built over time—not achieved through quick fixes.</p>
    <p>Our approach is centred around personalised care, attention to detail, and long-term results.</p>
    <p>We work with you to not only relieve symptoms, but to improve how your body functions and performs in everyday life.</p>
    <p>Every step of your journey is guided with care, clarity, and a focus on lasting wellbeing.</p>
  </div>
  <svg class="abs corner" width="140" height="120" viewBox="0 0 140 120"><path d="M140 0 C130 60 90 105 0 120 L140 120Z" fill="#0e8c7e"/></svg>
  <div class="abs page-num">03</div>
</section>

<section class="page plan">
  <div class="abs plan-panel">
    <h2 class="abs heading plan-title">YOUR <span class="accent">PERSONALISED CARE PLAN</span></h2>
    <div class="abs rule"></div>
    <div class="abs field-label" style="left:22px;top:90px">Patient Name:</div>
    <div class="abs field-line" style="left:22px;top:121px;width:213px"></div>
    <div class="abs field-label" style="left:22px;top:148px">Recommended Plan:</div>
    <div class="abs field-line" style="left:22px;top:182px;width:48px"></div>
    <div class="abs field-label" style="left:75px;top:174px">treatments over</div>
    <div class="abs field-line" style="left:140px;top:182px;width:55px"></div>
    <div class="abs field-label" style="left:200px;top:174px">weeks</div>
    <div class="abs field-label" style="left:22px;top:200px">Notes:</div>
    <div class="abs field-line" style="left:22px;top:237px;width:213px"></div>
    <div class="abs field-line" style="left:22px;top:263px;width:213px"></div>
    <div class="abs field-line" style="left:22px;top:289px;width:213px"></div>
    <div class="abs field-line" style="left:22px;top:316px;width:213px"></div>
  </div>
  <div class="abs contact-panel">
    <div class="abs brand-mark"></div>
    <div class="abs brand-name">FERNWELL PRACTICE</div>
    <div class="abs brand-sub">CHIROPRACTIC &amp; WELLNESS</div>
    <div class="abs script">We're here to support you</div>
    <div class="abs script-follow">every step of your journey.</div>
    <div class="abs rule"></div>
    <ul class="abs contact-list">
      <li><svg width="12" height="12" viewBox="0 0 12 12"><path d="M6 11 C3 7.5 2 5.8 2 4.3 a4 4 0 0 1 8 0 C10 5.8 9 7.5 6 11Z" fill="none" stroke="#0e8c7e" stroke-width="1.1"/><circle cx="6" cy="4.4" r="1.4" fill="none" stroke="#0e8c7e"/></svg>8/12 Linden Parade, Seacliff NSW 2105</li>
      <li><svg width="12" height="12" viewBox="0 0 12 12"><path d="M2.5 1.5 L4.5 1.5 L5.3 4 L4 5 C4.8 6.8 5.4 7.4 7 8 L8 6.7 L10.5 7.5 V9.5 C10.5 10 10 10.5 9.5 10.5 C5.5 10.2 1.8 6.5 1.5 2.5 C1.5 2 2 1.5 2.5 1.5Z" fill="none" stroke="#0e8c7e" stroke-width="1.1"/></svg>02 5550 1842</li>
      <li><svg width="12" height="12" viewBox="0 0 12 12"><circle cx="6" cy="6" r="4.8" fill="none" stroke="#0e8c7e" stroke-width="1.1"/><ellipse cx="6" cy="6" rx="2" ry="4.8" fill="none" stroke="#0e8c7e"/><path d="M1.2 6 H10.8" stroke="#0e8c7e"/></svg>fernwellpractice.com.au</li>
      <li><svg width="12" height="12" viewBox="0 0 12 12"><rect x="1" y="2.5" width="10" height="7" fill="none" stroke="#0e8c7e" stroke-width="1.1"/><path d="M1 2.5 L6 6.5 L11 2.5" fill="none" stroke="#0e8c7e"/></svg>care@fernwellpractice.com.au</li>
    </ul>
    <div class="abs socials"><span class="social-dot"></span><span class="social-dot"></span><span class="social-dot"></span></div>
    <div class="abs closing">
      <svg class="abs closing-icon" width="22" height="20" viewBox="0 0 22 20"><path d="M11 18 C4 13 1.5 9.5 1.5 6 a4.8 4.8 0 0 1 9.5-1 a4.8 4.8 0 0 1 9.5 1 C20.5 9.5 18 13 11 18Z" fill="none" stroke="#fff" stroke-width="1.4"/></svg>
      <p class="abs closing-text">Your health is a long-term investment—<br>and we're here to guide you every step of the way.</p>
      <p class="abs closing-script">Thank you for trusting us with your care.</p>
    </div>
  </div>
</section>

</body>
</html>
```